Letter Head Design

I need a letter head design based on my company logo that I attached.
Include phone number: (403)582-3140
Address: 417 Brindlewood Avenue NE, Calgary, Alberta, Canada, T3M 4K8

Industry/Entity Type

It Company

```html
<!DOCTYPE html>
<html lang="en">
<head>
<meta charset="utf-8">
<title>Lumenfield Interiors Corp. – Letterhead</title>
<link rel="stylesheet" href="https://fonts.googleapis.com/css2?family=Open+Sans:wght@400;600&family=Lato:wght@400&display=swap">
<style>
  :root {
    --backdrop: #e9e7e3;
    --paper: #ffffff;
    --brand-blue: #1c5fae;
    --brand-green: #5db446;
    --band-start: #6abd4a;
    --band-end: #4fa63e;
    --text-dark: #3a3a3a;
    --text-light: #ffffff;
    --divider: #9a9a9a;
  }
  html, body {
    margin: 0;
    padding: 0;
    width: 952px;
    height: 1200px;
    overflow: hidden;
    background: var(--backdrop);
  }
  .letterhead {
    position: absolute;
    left: 56px;
    top: 50px;
    width: 836px;
    height: 1083px;
    background: var(--paper);
    box-shadow: 0 1px 4px rgba(0,0,0,0.15);
    overflow: hidden;
  }
  .brand {
    position: absolute;
    left: 0;
    right: 0;
    top: 124px;
    display: flex;
    justify-content: center;
    align-items: center;
    gap: 10px;
  }
  .brand-square {
    width: 22px;
    height: 22px;
    background: var(--brand-green);
    border-radius: 3px;
  }
  .brand-name {
    font-family: "Open Sans", sans-serif;
    font-weight: 600;
    font-size: 26px;
    color: var(--brand-blue);
    letter-spacing: -0.3px;
  }
  .contact-phone {
    position: absolute;
    left: 704px;
    top: 79px;
    display: flex;
    align-items: center;
    gap: 6px;
    font-family: "Lato", sans-serif;
    font-size: 12.5px;
    color: var(--text-dark);
  }
  .contact-phone .divider {
    width: 1px;
    height: 24px;
    background: var(--divider);
  }
  .contact-phone svg { width: 10px; height: 10px; }
  .footer-rule {
    position: absolute;
    left: 0;
    right: 0;
    bottom: 76px;
    height: 2px;
    background: var(--brand-blue);
  }
  .footer-band {
    position: absolute;
    left: 0;
    right: 0;
    bottom: 0;
    height: 70px;
    background: linear-gradient(90deg, var(--band-start), var(--band-end));
  }
  .address {
    position: absolute;
    left: 41px;
    top: 1034px;
    margin: 0;
    font-family: "Lato", sans-serif;
    font-style: normal;
    font-weight: 400;
    font-size: 12px;
    line-height: 18px;
    color: var(--text-light);
  }
</style>
</head>
<body>
  <main class="letterhead">
    <header class="brand">
      <span class="brand-square"></span>
      <span class="brand-name">Lumenfield Interiors Corp.</span>
    </header>

    <div class="contact-phone">
      <span class="divider"></span>
      <svg viewBox="0 0 10 10" aria-hidden="true">
        <path d="M2 1 L4 1 L4.6 3 L3.5 3.8 C4 5 5 6 6.2 6.5 L7 5.4 L9 6 L9 8 C9 8.6 8.5 9 8 9 C4.5 9 1 5.5 1 2 C1 1.5 1.4 1 2 1 Z" fill="none" stroke="#3a3a3a" stroke-width="0.9"/>
      </svg>
      <span>(403)582-3140</span>
    </div>

    <div class="footer-rule"></div>
    <div class="footer-band"></div>

    <address class="address">
      417 Brindlewood Avenue NE<br>
      Calgary, Alberta, Canada, T3M 4K8
    </address>
  </main>
</body>
</html>
```